Hi! We require a design for business cards for directors and head teachers of an international daycare for children 0 - 9. We are family-owned, -operated and -oriented. We have six locations, looking to franchise. Our USPs are: 1) Flexibility 2) Quality teachers 3) International culture 4) Best nutrition We are quality teachers and professional caretakers, but with creativity and personality! Business cards should be playful (but no Comic Sans or baby hand prints), colorful (but no rainbows), and have some breathing space. It should be obvious from the business card that we're a daycare. In 2020 we'll be launching our new website based on this design: https://plomvane.io/47K2RQLWZTD The font in the new website will be Houschka (medium, demibold, bold). We will keep our current logo, included in the files here. There are also screenshots of some designs we like. Show us your best! :)

Industry/Entity Type

Childcare

Contact Information for Business Card

Lotte de Vries-Bakhuis
Communications Wizard
Poppel Hoek International Daycare
Kastanjeweg 47 B, 2316 KR Leiden
www.poppelhoek.nl
+31 647315082

Font styles to use
Serif
Sans Serif

Colors

Designer to choose colors to be used in the design.

Requirements
Must have
• Color

```html
<!DOCTYPE html>
<html lang="en">
<head>
<meta charset="utf-8">
<title>Poppel Hoek – Business Card</title>
<link href="https://fonts.googleapis.com/css2?family=Work+Sans:wght@400;500;700;800&display=swap" rel="stylesheet">
<style>
  :root {
    --backdrop: #3b3431;
    --card: #1b1b1c;
    --accent-pink: #e8548e;
    --accent-blue: #27a9e1;
    --text-light: #f2f2f2;
    --shadow: rgba(0, 0, 0, 0.45);
  }
  * { box-sizing: border-box; margin: 0; padding: 0; }
  html, body {
    width: 1200px;
    height: 716px;
    overflow: hidden;
    background: var(--backdrop);
    font-family: "Work Sans", sans-serif;
  }
  .stage {
    width: 1200px;
    height: 716px;
    display: flex;
    align-items: center;
    justify-content: center;
    gap: 40px;
  }
  .card {
    position: relative;
    width: 540px;
    height: 310px;
    background: var(--card);
    box-shadow: 0 10px 30px var(--shadow);
  }
  .brand {
    display: flex;
    align-items: center;
    gap: 14px;
  }
  .brand-dot {
    width: 30px;
    height: 30px;
    border-radius: 50%;
    background: var(--accent-blue);
    flex: none;
  }
  .brand-name {
    font-weight: 800;
    color: var(--accent-pink);
    line-height: 0.95;
    text-transform: uppercase;
  }
  .brand-line { display: block; }
  .brand-line--main { font-size: 48px; letter-spacing: 1px; }
  .brand-line--sub { font-size: 12.5px; letter-spacing: 1.6px; margin-top: 8px; }

  .card--front {
    display: flex;
    align-items: center;
    justify-content: center;
  }

  .card--back .brand {
    position: absolute;
    left: 40px;
    top: 50%;
    transform: translateY(-50%);
    gap: 11px;
  }
  .card--back .brand-dot { width: 22px; height: 22px; }
  .card--back .brand-line--main { font-size: 36px; letter-spacing: 0.5px; }
  .card--back .brand-line--sub { font-size: 9.5px; letter-spacing: 1.1px; margin-top: 6px; }

  .divider {
    position: absolute;
    left: 282px;
    top: 70px;
    width: 2px;
    height: 170px;
    background: var(--accent-blue);
  }
  .contact {
    position: absolute;
    left: 306px;
    top: 76px;
    color: var(--text-light);
    font-size: 13px;
    line-height: 1.4;
  }
  .contact-name {
    color: var(--accent-blue);
    font-weight: 500;
    font-size: 15px;
    text-transform: uppercase;
    letter-spacing: 0.4px;
    white-space: nowrap;
  }
  .contact-role { margin-bottom: 10px; }
  .contact-address { margin-bottom: 10px; }
  .contact-line {
    display: flex;
    align-items: center;
    gap: 7px;
  }
  .contact-icon {
    width: 10px;
    height: 10px;
    flex: none;
  }
</style>
</head>
<body>
  <main class="stage">
    <section class="card card--front">
      <div class="brand">
        <span class="brand-dot"></span>
        <span class="brand-name">
          <span class="brand-line brand-line--main">Poppel</span>
          <span class="brand-line brand-line--main">Hoek</span>
          <span class="brand-line brand-line--sub">International Daycare</span>
        </span>
      </div>
    </section>

    <section class="card card--back">
      <div class="brand">
        <span class="brand-dot"></span>
        <span class="brand-name">
          <span class="brand-line brand-line--main">Poppel</span>
          <span class="brand-line brand-line--main">Hoek</span>
          <span class="brand-line brand-line--sub">International Daycare</span>
        </span>
      </div>
      <div class="divider"></div>
      <div class="contact">
        <p class="contact-name">Lotte de Vries-Bakhuis</p>
        <p class="contact-role">Communications Wizard</p>
        <p class="contact-address">Kastanjeweg 47 B,<br>2316 KR Leiden</p>
        <p class="contact-line">
          <svg class="contact-icon" viewBox="0 0 10 10" aria-hidden="true"><path d="M2 0.5 L3.6 0.5 L4.2 3 L3 3.8 Q4 6 6.2 7 L7 5.8 L9.5 6.4 L9.5 8 Q9.5 9.5 8 9.5 Q0.5 9 0.5 2 Q0.5 0.5 2 0.5 Z" fill="var(--accent-blue)"/></svg>
          +31 647315082
        </p>
        <p class="contact-line">
          <svg class="contact-icon" viewBox="0 0 10 10" aria-hidden="true"><rect x="0.75" y="2" width="8.5" height="6" fill="none" stroke="var(--accent-blue)" stroke-width="1.2"/><path d="M0.75 2 L5 5.5 L9.25 2" fill="none" stroke="var(--accent-blue)" stroke-width="1.2"/></svg>
          info@poppelhoek.nl
        </p>
        <p class="contact-line">
          <svg class="contact-icon" viewBox="0 0 10 10" aria-hidden="true"><circle cx="5" cy="5" r="4.3" fill="none" stroke="var(--accent-blue)" stroke-width="1.1"/><ellipse cx="5" cy="5" rx="1.8" ry="4.3" fill="none" stroke="var(--accent-blue)" stroke-width="0.9"/><path d="M0.7 5 H9.3" stroke="var(--accent-blue)" stroke-width="0.9"/></svg>
          www.poppelhoek.nl
        </p>
      </div>
    </section>
  </main>
</body>
</html>
```